Start-up consultancy in Healthcare Space requiring clean and crisp website design

I am the founder of a start-up consultancy to improve access to medicines and healthcare around the globe. My primary product are consulting services to both the public sector and the private sector to work on: improved healthcare delivery, the right price for medicines and addressing challenges in emerging markets. As the sector is fairly conservative, I need a clean and very professional website as is should signal competence in the sector. Therefore, I like shades of white and green but there should be a link to healthcare. Please see the logo that is featured on my business cards.

Target Market(s)

Ministry of Health, Pharmaceutical companies, Emerging Markets (Latin America, Middle East, Eastern Europe, Asia)

Industry/Entity Type

Healthcare

Coding

Coded - Design and coding required

Number of Pages Required

5+ page

Font styles to use
Serif

Colors

Designer to choose colors to be used in the design.

Requirements
Must have
• About Section
• Services Section
• Blog Section
• The website design should also portray the solution for access to healthcare and highlight my ability to help clients with that.
• The website will be hosted on a CMS and should therefore be easy to adjust. I would prefer wordpress but open to any suggestions as I have my own webspace.
• I quite like these websites:
• https://www.tevluma.com/why-tevluma
• https://home.quillfernwell.com/
Nice to have
• I like to see some creative thinking with the theme of healthcare.
Should not have
• The design should not feature too many hospitals or pills etc. as this is really not my focus.

```html
<!DOCTYPE html>
<html lang="en">
<head>
<meta charset="utf-8">
<title>Verdanel Consulting — Home</title>
<link rel="stylesheet" href="https://fonts.googleapis.com/css2?family=Nunito+Sans:wght@700;800&family=Open+Sans:wght@700&family=Carlito&display=swap">
<style>
  :root {
    --frame: #e4e4e4;
    --page: #ffffff;
    --brand-green: #0b6433;
    --nav-green: #66a084;
    --nav-active: #0d5a6e;
    --nav-text: #c9f1ee;
    --heading-grey: #5b5b5b;
    --body-grey: #4f4f4f;
    --hero-light: #e9ecef;
    --hero-mid: #c8d0da;
    --hero-blue: #6f8fc8;
    --button-face: #dde9ee;
    --button-edge: #8fb2c2;
    --button-text: #3e4a50;
    --tick-fill: #6f86d6;
  }
  * { box-sizing: border-box; margin: 0; padding: 0; }
  html, body { width: 1171px; height: 1200px; overflow: hidden; background: var(--frame); }
  .page {
    position: absolute; left: 15px; top: 15px; width: 1141px; height: 1171px;
    background: var(--page);
  }
  .site-header { height: 107px; position: relative; }
  .brand {
    position: absolute; left: 31px; top: 24px;
    display: flex; align-items: center; gap: 10px;
    font-family: "Nunito Sans", sans-serif; font-weight: 800;
    font-size: 22px; letter-spacing: 1px; color: var(--brand-green);
  }
  .brand-square { width: 22px; height: 22px; background: var(--brand-green); }
  .main-nav {
    height: 41px; background: var(--nav-green);
    display: flex; padding-left: 158px;
    font-family: "Nunito Sans", sans-serif; font-weight: 800; font-size: 16px;
  }
  .main-nav a {
    color: var(--nav-text); text-decoration: none;
    display: flex; align-items: center; justify-content: center; height: 100%;
  }
  .main-nav a.is-active { background: var(--nav-active); color: #fff; width: 139px; }
  .nav-story { width: 162px; }
  .nav-people { width: 172px; }
  .nav-services { width: 175px; }
  .nav-contact { width: 175px; }
  .hero {
    height: 496px;
    background:
      radial-gradient(ellipse 260px 300px at 290px 300px, #f4f5f6 0%, rgba(244,245,246,0) 70%),
      radial-gradient(ellipse 150px 240px at 1030px 360px, var(--hero-blue) 0%, rgba(111,143,200,0) 75%),
      linear-gradient(90deg, var(--hero-light) 0%, var(--hero-mid) 55%, #d7dde3 100%);
  }
  .mission {
    height: 97px; background: var(--brand-green);
    display: flex; align-items: center; justify-content: center; text-align: center;
    font-family: "Open Sans", sans-serif; font-weight: 700; font-size: 18px; line-height: 22px;
    color: #fff;
  }
  .story { text-align: center; padding-top: 52px; }
  .story h2 {
    font-family: "Nunito Sans", sans-serif; font-weight: 800; font-size: 26px;
    color: var(--heading-grey); letter-spacing: 0.3px;
  }
  .story p {
    font-family: "Carlito", sans-serif; font-size: 16.5px; line-height: 19.5px;
    color: var(--body-grey); width: 1030px; margin: 0 auto;
  }
  .story h2 + p { margin-top: 38px; }
  .story p + p { margin-top: 19.5px; }
  .discover-button {
    display: inline-flex; align-items: center; gap: 14px;
    margin-top: 33px; width: 226px; height: 45px; padding-left: 10px;
    border-radius: 23px; border: 2px solid var(--button-edge);
    background: linear-gradient(180deg, #f6fafb 0%, var(--button-face) 55%, #c7d8df 100%);
    font-family: "Nunito Sans", sans-serif; font-weight: 800; font-size: 17px;
    color: var(--button-text); text-decoration: none;
  }
  .site-footer {
    position: absolute; left: 0; bottom: 0; width: 100%; height: 34px;
    background: var(--brand-green); color: #fff;
    display: flex; align-items: center; justify-content: center;
    font-family: "Open Sans", sans-serif; font-weight: 700; font-size: 11.5px;
  }
</style>
</head>
<body>
<div class="page">
  <header class="site-header">
    <div class="brand"><span class="brand-square"></span>VERDANEL CONSULTING</div>
  </header>
  <nav class="main-nav">
    <a class="is-active" href="#">HOME</a>
    <a class="nav-story" href="#">OUR STORY</a>
    <a class="nav-people" href="#">OUR PEOPLE</a>
    <a class="nav-services" href="#">WHAT WE DO</a>
    <a class="nav-contact" href="#">CONTACT</a>
  </nav>
  <div class="hero" role="img" aria-label="Photograph of a smiling doctor with a stethoscope in front of blurred medical colleagues"></div>
  <section class="mission">
    <p>My primary product are consulting services to both the public sector and the private sector to work on:<br>improved healthcare delivery, the right price for medicines and addressing challenges in emerging markets.</p>
  </section>
  <section class="story">
    <h2>OUR STORY</h2>
    <p>Lorem ipsum dolor sit amet, consectetuer adipiscing elit, sed diam nonummy nibh euismod tincidunt ut laoreet dolore magna aliquam erat volutpat. Ut wisi enim ad minim veniam, quis nostrud exerci tation ullamcorper suscipit lobortis nisl ut aliquip ex ea commodo consequat. Duis autem vel eum iriure dolor in hendrerit in vulputate velit esse molestie consequat, vel illum dolore eu feugiat nulla facilisis at vero eros et accumsan et iusto odio dignissim qui blandit praesent luptatum zzril delenit augue duis dolore te feugait nulla facilisi.</p>
    <p>Nam liber tempor cum soluta nobis eleifend option congue nihil imperdiet doming id quod mazim placerat facer possim assum. Typi non habent claritatem insitam; est usus legentis in iis qui facit eorum claritatem. Investigationes demonstraverunt lectores legere me lius quod ii legunt saepius. Claritas est etiam processus dynamicus, qui sequitur mutationem consuetudium lectorum.</p>
    <a class="discover-button" href="#">
      <svg width="28" height="28" viewBox="0 0 28 28" aria-hidden="true">
        <circle cx="14" cy="14" r="12" fill="var(--tick-fill)" stroke="#fff" stroke-width="2"/>
        <path d="M8.5 14.5l3.8 3.6 7.2-8" fill="none" stroke="#fff" stroke-width="2.6" stroke-linecap="round" stroke-linejoin="round"/>
      </svg>
      DISCOVER MORE
    </a>
  </section>
  <footer class="site-footer">COPYRIGHT © 2017 VERDANEL CONSULTING. ALL RIGHTS RESERVED.</footer>
</div>
</body>
</html>
```